Brightvale Cherries Rainier POS Card 7"H x 11"W

We are wanting to create a one-sided 7 x 11 Rainier cherry card that is eye catching and informative.This should be clear and easy to read and not cluttered. We use these cards as a display in grocery stores, demo stands, and other events to market Brightvale Rainier Cherries. We have a few facts that we would like displayed on the card (see below).

Target Market(s)

Consumers

Industry/Entity Type

Agriculture

Font styles to use
Sans Serif

Requirements
Must have
• Yellow cherries - yellow fruit (the blush on the skin is a kiss from the sun)
• Juice doesn't stain - Kid Friendly
• Add contrast to your summer table
• Sweetest Variety - still low glycemic
• Source of Vitamin C, Source of Potassium, and Source of Melatonin
• Rainiers take up to 4x as much work as red cherries
• Natural Color palettes
• Easy to read
• Brightvale Cherries
Nice to have
• Unique, creative, realistc Rainier cherry designs
Should not have
• pastel or neon color scheme, overly cutesy elements

```html
<!DOCTYPE html>
<html lang="en">
<head>
<meta charset="utf-8">
<title>Brightvale Cherries – Yellow Cherries Card</title>
<link rel="stylesheet" href="https://fonts.googleapis.com/css2?family=Arvo:wght@700&family=Cherry+Swash:wght@700&display=swap">
<style>
  :root {
    --sun-yellow: #f7c90c;
    --band-yellow: #f9d30d;
    --cherry-red: #c8202b;
    --badge-red: #c62030;
    --badge-orange: #f19b3c;
    --ink: #1e1a17;
    --white: #ffffff;
    --photo-warm: #d9763e;
    --photo-gold: #eeb456;
    --wood-dark: #4a3326;
    --wood-mid: #7a5a45;
  }
  * { margin: 0; padding: 0; box-sizing: border-box; }
  html, body { width: 1200px; height: 764px; overflow: hidden; background: var(--white); }
  .card { position: relative; width: 1200px; height: 764px; background: var(--white); overflow: hidden; }

  .sprig-art {
    position: absolute; left: 138px; top: 40px; width: 122px; height: 118px;
    border-radius: 16px;
    background: linear-gradient(160deg, #fbe27a 0%, var(--sun-yellow) 100%);
  }
  .headline {
    position: absolute; left: 270px; top: 30px;
    font-family: "Arvo", serif; font-weight: 700; font-size: 68px; line-height: 1;
    color: var(--sun-yellow); letter-spacing: 1px; white-space: nowrap;
  }
  .tagline {
    position: absolute; left: 265px; top: 122px;
    font-family: "Arvo", serif; font-weight: 700; font-size: 33px; line-height: 1;
    color: var(--cherry-red); letter-spacing: 1.5px; white-space: nowrap;
  }

  .fact-band {
    position: absolute; left: 0; top: 170px; width: 1200px; height: 213px;
    background: var(--band-yellow);
  }
  .brand {
    position: absolute; left: 72px; top: 54px; width: 400px;
    display: flex; align-items: center; gap: 20px;
  }
  .brand-dot { flex: none; width: 56px; height: 56px; border-radius: 50%; background: var(--cherry-red); }
  .brand-name {
    font-family: "Cherry Swash", sans-serif; font-weight: 700; font-size: 46px;
    color: var(--ink); line-height: 1.05;
  }
  .fact-list {
    position: absolute; left: 505px; top: 26px; list-style: none;
    font-family: "Cherry Swash", sans-serif; font-weight: 700; font-size: 22.5px;
    line-height: 30.5px; color: var(--ink); white-space: nowrap;
  }
  .fact-list li { position: relative; padding-left: 16px; }
  .fact-list li::before {
    content: ""; position: absolute; left: 0; top: 11px;
    width: 9px; height: 9px; border-radius: 50%; background: var(--cherry-red);
  }

  .cherry-photo {
    position: absolute; left: 0; top: 383px; width: 1200px; height: 381px;
    background: linear-gradient(160deg, var(--wood-mid) 0%, var(--photo-warm) 35%, var(--photo-gold) 55%, var(--photo-warm) 75%, var(--wood-dark) 100%);
  }

  .badge {
    position: absolute; width: 162px; height: 162px; border-radius: 50%;
    display: flex; align-items: center; justify-content: center; text-align: center;
    font-family: "Cherry Swash", sans-serif; font-weight: 700; font-size: 27px;
    line-height: 1.2; color: var(--white);
  }
  .badge-kid { left: 975px; top: 399px; background: var(--badge-red); }
  .badge-glycemic { left: 981px; top: 578px; background: var(--badge-orange); }
</style>
</head>
<body>
  <main class="card">
    <div class="sprig-art" role="img" aria-label="Drawn sprig of yellow cherries with leaves"></div>
    <h1 class="headline">Yellow Cherries</h1>
    <p class="tagline">the blush on the skin is a kiss from the sun</p>

    <section class="fact-band">
      <div class="brand">
        <span class="brand-dot"></span>
        <span class="brand-name">Brightvale<br>Cherries</span>
      </div>
      <ul class="fact-list">
        <li>Juice doesn't stain. Kid Friendly</li>
        <li>Add contrast to your summer table</li>
        <li>Sweetest Variety. Still low glycemic</li>
        <li>Source of Vitamin C, Potassium, and Melatonin</li>
        <li>Rainiers take up to 4x as much work as red cherries</li>
      </ul>
    </section>

    <div class="cherry-photo" role="img" aria-label="Photo of a woven basket full of yellow and blushed Rainier cherries on a rustic wooden table"></div>

    <div class="badge badge-kid">Kid<br>Friendly</div>
    <div class="badge badge-glycemic">Still Low<br>Glycemic</div>
  </main>
</body>
</html>
```